1 Page Sales Brochure of our Services

I need to create a one page brochure that our sales team can take into meetings about our services - Need this to be an impressive one page that looks fresh and new using our brand colors of Brindle green, black and white. Our brand looks "clean" think Marlo brand in how everything is clean and white and crisp. Our website showcases our services: https://brindlesports.example/services/ --- After done with this project I would like to create a full booklet. Want to begin with this project first.

Target Market(s)

State of Texas

Industry/Entity Type

Sports Construction in Texas Only

Font styles to use
Serif

Colors
00AB8E
00BBA5
67D7C9
C6EFE9
E9F9F6

Requirements
Must have
• Front and Back and cover our services outlined on our website: https://brindlesports.example/services/
Nice to have
• Need one that can get sent digital and printed -- Our colors are the Brindle green, white and black - We want brochure to look clean, almost like the Marlo feel of their product's branding

```html
<!DOCTYPE html>
<html lang="en">
<head>
<meta charset="utf-8">
<title>Brindle Sports Construction – Services Brochure</title>
<link href="https://fonts.googleapis.com/css2?family=Bebas+Neue&family=Montserrat:wght@400;500;600;700&display=swap" rel="stylesheet">
<style>
  :root {
    --brand-green: #0e6b35;
    --brand-green-dark: #0b5a2c;
    --ink: #161616;
    --body-text: #3a3a3a;
    --paper: #f6f6f6;
    --paper-edge: #ececec;
    --backdrop: #e4e4e4;
    --white: #ffffff;
  }
  * { box-sizing: border-box; margin: 0; padding: 0; }
  html, body { width: 1200px; height: 1200px; overflow: hidden; background: var(--backdrop); }
  .stage { position: absolute; left: 0; top: 0; width: 1932px; height: 1932px; transform: scale(0.62112); transform-origin: 0 0; }
  .sheet { position: absolute; top: 378px; width: 831px; height: 1174px;
    background: linear-gradient(180deg, var(--paper) 0%, var(--paper-edge) 100%);
    font-family: "Montserrat", sans-serif; color: var(--ink); }
  .sheet--front { left: 109px; }
  .sheet--back { left: 992px; }
  .abs { position: absolute; }

  .brand-name { left: 28px; top: 46px; display: flex; align-items: center; gap: 12px;
    font-weight: 600; font-size: 54px; color: var(--brand-green); letter-spacing: -1px; }
  .brand-name .mark-dot { width: 28px; height: 28px; border-radius: 50%; background: var(--brand-green); }

  .follow { left: 490px; top: 38px; display: flex; align-items: center; gap: 8px; }
  .follow .social { width: 32px; height: 32px; border-radius: 5px; background: var(--brand-green); }
  .follow .label { margin-left: 6px; font-weight: 600; font-size: 20px; }
  .follow-rule { left: 490px; top: 82px; width: 74px; height: 3px; background: var(--ink); }
  .address { left: 490px; top: 96px; display: flex; gap: 12px; align-items: flex-start; font-size: 17px; line-height: 20px; letter-spacing: .4px; }
  .address .pin { width: 32px; height: 32px; border-radius: 5px; background: var(--brand-green); display: flex; align-items: center; justify-content: center; margin-top: 2px; }
  .address b { font-weight: 700; }

  .headline-banner { left: 25px; top: 160px; width: 781px; height: 76px; border-radius: 10px; background: var(--brand-green);
    color: var(--white); font-family: "Bebas Neue", sans-serif; font-weight: 400; font-size: 68px; text-align: center; line-height: 80px; letter-spacing: 2px; }

  .photo { border: 3px solid var(--white); border-radius: 10px; box-shadow: 0 0 0 1px #d8d8d8; }
  .photo--ballparks { left: 25px; top: 250px; width: 780px; height: 274px;
    background: linear-gradient(160deg, #8a9a6a 0%, #4f8a3c 35%, #2f8a3a 60%, #6e4a3a 80%, #3e7a36 100%); }
  .photo--stadium-aerial { left: 25px; top: 663px; width: 377px; height: 320px;
    background: linear-gradient(170deg, #c8c8c0 0%, #d9dcd6 35%, #3d7b3a 60%, #6b6b5a 100%); }
  .photo--site-grading { left: 27px; top: 162px; width: 779px; height: 276px;
    background: linear-gradient(165deg, #8a8a66 0%, #c9b58d 35%, #b6b2a8 60%, #9d9a92 100%); }
  .photo--mascot { left: 27px; top: 452px; width: 202px; height: 207px;
    background: linear-gradient(180deg, #4a5560 0%, #2f6a3a 55%, #3f8a3e 100%); }

  .intro-copy { left: 40px; top: 545px; width: 751px; font-size: 13.4px; line-height: 18.3px; color: var(--body-text); text-align: center; letter-spacing: .3px; }
  .section-rule { left: 25px; top: 636px; width: 781px; height: 3px; background: var(--brand-green); }

  .testimonial { left: 38px; top: 847px; width: 352px; height: 183px; border-radius: 10px; background: var(--brand-green); color: var(--white); padding: 14px 12px; }
  .testimonial .quote-mark { position: absolute; left: 12px; top: 10px; font-family: "Bebas Neue", sans-serif; font-size: 44px; line-height: 44px; }
  .testimonial .frame { position: absolute; left: 12px; top: 32px; width: 328px; height: 136px; border: 2px solid var(--white); border-top: none; border-radius: 0 0 4px 4px; }
  .testimonial .frame::before { content: ""; position: absolute; left: 28px; right: -2px; top: 0; height: 2px; background: var(--white); }
  .testimonial p { position: absolute; left: 24px; top: 44px; width: 310px; font-size: 13px; line-height: 17px; letter-spacing: .4px; }
  .testimonial cite { position: absolute; left: 24px; top: 132px; font-style: normal; font-family: "Bebas Neue", sans-serif; font-size: 16px; letter-spacing: .5px; }

  .section-title { font-family: "Bebas Neue", sans-serif; font-weight: 400; font-size: 58px; line-height: 52px; color: var(--ink); letter-spacing: 1px; }
  .title-rule { width: 120px; height: 3px; background: var(--brand-green); }
  .copy { font-size: 13px; line-height: 18.2px; color: var(--body-text); letter-spacing: .35px; }
  .copy p + p { margin-top: 11px; }

  .contact-tab { top: 1054px; left: 38px; width: 146px; height: 40px; background: var(--white); border-radius: 8px 8px 0 0;
    font-weight: 500; font-size: 20px; line-height: 40px; text-align: center; z-index: 2; }
  .contact-bar { left: 25px; top: 1073px; width: 781px; height: 76px; border-radius: 12px; background: var(--brand-green);
    color: var(--white); display: flex; align-items: center; justify-content: space-between; padding: 10px 14px 0 13px; }
  .contact-bar .item { display: flex; align-items: center; gap: 8px; font-size: 14px; letter-spacing: .2px; white-space: nowrap; }
  .contact-bar .item--phone { font-size: 17px; font-weight: 600; }
  .contact-bar .icon { flex: none; width: 32px; height: 32px; border-radius: 6px; background: var(--white); display: flex; align-items: center; justify-content: center; }
  .contact-bar .divider { flex: none; width: 2px; height: 32px; background: var(--white); }

  .services-box { left: 428px; top: 672px; width: 378px; height: 370px; border-radius: 10px; background: linear-gradient(160deg, var(--brand-green) 0%, var(--brand-green-dark) 100%); color: var(--white); padding: 22px 24px; }
  .services-box h3 { font-family: "Bebas Neue", sans-serif; font-weight: 400; font-size: 36px; line-height: 36px; letter-spacing: 1px; }
  .services-box .rule { width: 120px; height: 3px; background: var(--white); margin: 8px 0 14px; }
  .services-box li { list-style: none; display: flex; align-items: center; gap: 6px; font-size: 17px; font-weight: 600; letter-spacing: .8px; height: 33.6px; }
  .services-box .tick { width: 13px; height: 13px; background: var(--white); border-radius: 2px; display: flex; align-items: center; justify-content: center; }
  .subhead { font-weight: 600; font-size: 16.5px; line-height: 20px; letter-spacing: .8px; }
</style>
</head>
<body>
<div class="stage">

  <!-- FRONT -->
  <section class="sheet sheet--front">
    <div class="abs brand-name"><span class="mark-dot"></span>Brindle</div>
    <div class="abs follow"><span class="social"></span><span class="social"></span><span class="social"></span><span class="label">Follow Us</span></div>
    <div class="abs follow-rule"></div>
    <div class="abs address">
      <span class="pin"><svg width="16" height="18" viewBox="0 0 16 18"><path d="M8 1a6 6 0 0 0-6 6c0 4.5 6 10 6 10s6-5.5 6-10a6 6 0 0 0-6-6z" fill="none" stroke="#fff" stroke-width="1.6"/><circle cx="8" cy="7" r="2" fill="none" stroke="#fff" stroke-width="1.6"/></svg></span>
      <span><b>418</b> North Cedar Street<br>Brookfield, <b>Texas 75001</b></span>
    </div>

    <h1 class="abs headline-banner">Building to a Higher Standard</h1>
    <div class="abs photo photo--ballparks" role="img" aria-label="Aerial view of striped baseball and softball fields with tennis courts and parking"></div>

    <p class="abs intro-copy">Since 2010, Brindle Sports Construction has been on the cutting edge of sports construction and design. Founded by Carter R. Lowe, we are one of the largest, most respected sports construction companies in the nation. Our client rapport and satisfaction rate speaks to the quality, integrity, and timely completion you can expect by partnering with us.</p>
    <div class="abs section-rule"></div>

    <div class="abs photo photo--stadium-aerial" role="img" aria-label="Aerial view of a high school football stadium with grandstands"></div>
    <blockquote class="abs testimonial">
      <span class="quote-mark">“</span>
      <span class="frame"></span>
      <p>Brindle is an outstanding company that takes pride in their work and in their customer's experience. They are commited to finishing the job in a timely manner and no detail is too small.</p>
      <cite>– Dale Hoskins, (Athletic Director, Pecan Creek ISD)</cite>
    </blockquote>

    <h2 class="abs section-title" style="left:428px;top:660px;">We're Here<br>To Serve You!</h2>
    <div class="abs title-rule" style="left:428px;top:769px;"></div>
    <div class="abs copy" style="left:428px;top:787px;width:372px;">
      <p>Brindle is more than just a company, we are a family working together to build amazing projects while having fun and serving people. We believe in the relationships we cultivate and the synergy it creates. We also realize that we do not live in a perfect world and work-hard to bring about positive change, one project at a time. Brindle works hard to maintain a strong balance sheet &amp; remains debt free and we take pride in our ability to pass this value on to our customers.</p>
      <p>Brindle is the exclusive TerraTurf partner in Texas. TerraTurf is the leading turf manufacturer in the US, known for durability, quality, and playability.</p>
    </div>

    <div class="abs contact-tab">Contact Us</div>
    <div class="abs contact-bar">
      <span class="item item--phone"><span class="icon"><svg width="18" height="18" viewBox="0 0 24 24"><path d="M5 3h4l2 5-2.5 1.5a11 11 0 0 0 6 6L16 13l5 2v4a2 2 0 0 1-2 2A16 16 0 0 1 3 5a2 2 0 0 1 2-2z" fill="none" stroke="#161616" stroke-width="1.6"/></svg></span>903.555.0147</span>
      <span class="divider"></span>
      <span class="item"><span class="icon"><svg width="18" height="14" viewBox="0 0 18 14"><rect x="1" y="1" width="16" height="12" fill="none" stroke="#161616" stroke-width="1.5"/><path d="M1 1l8 7 8-7" fill="none" stroke="#161616" stroke-width="1.5"/></svg></span>info@brindlesports.example</span>
      <span class="divider"></span>
      <span class="item"><span class="icon"><svg width="18" height="18" viewBox="0 0 20 20"><circle cx="10" cy="10" r="8" fill="none" stroke="#161616" stroke-width="1.5"/><ellipse cx="10" cy="10" rx="3.5" ry="8" fill="none" stroke="#161616" stroke-width="1.5"/><path d="M2 10h16M3.5 6h13M3.5 14h13" stroke="#161616" stroke-width="1.3"/></svg></span>www.brindlesports.example</span>
    </div>
  </section>

  <!-- BACK -->
  <section class="sheet sheet--back">
    <div class="abs brand-name"><span class="mark-dot"></span>Brindle</div>
    <div class="abs follow"><span class="social"></span><span class="social"></span><span class="social"></span><span class="label">Follow Us</span></div>
    <div class="abs follow-rule"></div>
    <div class="abs address">
      <span class="pin"><svg width="16" height="18" viewBox="0 0 16 18"><path d="M8 1a6 6 0 0 0-6 6c0 4.5 6 10 6 10s6-5.5 6-10a6 6 0 0 0-6-6z" fill="none" stroke="#fff" stroke-width="1.6"/><circle cx="8" cy="7" r="2" fill="none" stroke="#fff" stroke-width="1.6"/></svg></span>
      <span><b>418</b> North Cedar Street<br>Brookfield, <b>Texas 75001</b></span>
    </div>

    <div class="abs photo photo--site-grading" role="img" aria-label="Aerial view of a stadium under construction with graded field and grandstands"></div>
    <div class="abs photo photo--mascot" role="img" aria-label="Team mascot costume standing on a stadium field"></div>

    <h2 class="abs section-title" style="left:254px;top:462px;">About Brindle</h2>
    <div class="abs title-rule" style="left:254px;top:518px;"></div>
    <p class="abs copy" style="left:254px;top:536px;width:525px;">Brindle was founded in 2010 with one primary goal in mind, glorifying God by setting the standard in sports construction. Since then, we have been trusted to build hundreds of high-profile projects, including 7 pro league fields and dozens of college fields and have evolved into a much larger construction company with the ability to facilitate a turnkey approach to sports construction.</p>

    <h2 class="abs section-title" style="left:37px;top:685px;">Services</h2>
    <div class="abs title-rule" style="left:37px;top:740px;"></div>
    <h3 class="abs subhead" style="left:37px;top:758px;width:360px;">TURNKEY SOLUTIONS FOR SPORTS CONSTRUCTION</h3>
    <div class="abs copy" style="left:37px;top:806px;width:370px;">
      <p>Brindle Sports Construction offers turnkey solutions in the realm of general sports construction. We're committed to excellence in all we do, and we seek to develop lasting relationships with our clients. Brindle is not in the business to win a single job and move on. We are working to earn your trust and business as we want you as a customer for life.</p>
      <p>At Brindle we have 7 Proverbs we strive to live by. Our #1 proverb is to "Deliver On Our Promises". That is our promise to you that we will strive to deliver on time with the quality and service you expect and deserve on every job.</p>
    </div>

    <div class="abs services-box">
      <h3>Our Services Include :</h3>
      <div class="rule"></div>
      <ul>
        <li><span class="tick"><svg width="9" height="8" viewBox="0 0 9 8"><path d="M1 4l2.5 2.5L8 1" fill="none" stroke="#0e6b35" stroke-width="1.8"/></svg></span>Track Construction</li>
        <li><span class="tick"><svg width="9" height="8" viewBox="0 0 9 8"><path d="M1 4l2.5 2.5L8 1" fill="none" stroke="#0e6b35" stroke-width="1.8"/></svg></span>Natural Grass Fields</li>
        <li><span class="tick"><svg width="9" height="8" viewBox="0 0 9 8"><path d="M1 4l2.5 2.5L8 1" fill="none" stroke="#0e6b35" stroke-width="1.8"/></svg></span>Synthetic Field Construction</li>
        <li><span class="tick"><svg width="9" height="8" viewBox="0 0 9 8"><path d="M1 4l2.5 2.5L8 1" fill="none" stroke="#0e6b35" stroke-width="1.8"/></svg></span>Stadium Construction</li>
        <li><span class="tick"><svg width="9" height="8" viewBox="0 0 9 8"><path d="M1 4l2.5 2.5L8 1" fill="none" stroke="#0e6b35" stroke-width="1.8"/></svg></span>Tennis Court Construction</li>
        <li><span class="tick"><svg width="9" height="8" viewBox="0 0 9 8"><path d="M1 4l2.5 2.5L8 1" fill="none" stroke="#0e6b35" stroke-width="1.8"/></svg></span>Service + Maintenance</li>
        <li><span class="tick"><svg width="9" height="8" viewBox="0 0 9 8"><path d="M1 4l2.5 2.5L8 1" fill="none" stroke="#0e6b35" stroke-width="1.8"/></svg></span>Stadium Lighting</li>
        <li><span class="tick"><svg width="9" height="8" viewBox="0 0 9 8"><path d="M1 4l2.5 2.5L8 1" fill="none" stroke="#0e6b35" stroke-width="1.8"/></svg></span>Surface Maintenance + Repair</li>
      </ul>
    </div>

    <div class="abs contact-tab">Contact Us</div>
    <div class="abs contact-bar">
      <span class="item item--phone"><span class="icon"><svg width="18" height="18" viewBox="0 0 24 24"><path d="M5 3h4l2 5-2.5 1.5a11 11 0 0 0 6 6L16 13l5 2v4a2 2 0 0 1-2 2A16 16 0 0 1 3 5a2 2 0 0 1 2-2z" fill="none" stroke="#161616" stroke-width="1.6"/></svg></span>903.555.0147</span>
      <span class="divider"></span>
      <span class="item"><span class="icon"><svg width="18" height="14" viewBox="0 0 18 14"><rect x="1" y="1" width="16" height="12" fill="none" stroke="#161616" stroke-width="1.5"/><path d="M1 1l8 7 8-7" fill="none" stroke="#161616" stroke-width="1.5"/></svg></span>info@brindlesports.example</span>
      <span class="divider"></span>
      <span class="item"><span class="icon"><svg width="18" height="18" viewBox="0 0 20 20"><circle cx="10" cy="10" r="8" fill="none" stroke="#161616" stroke-width="1.5"/><ellipse cx="10" cy="10" rx="3.5" ry="8" fill="none" stroke="#161616" stroke-width="1.5"/><path d="M2 10h16M3.5 6h13M3.5 14h13" stroke="#161616" stroke-width="1.3"/></svg></span>www.brindlesports.example</span>
    </div>
  </section>

</div>
</body>
</html>
```